Makeup Artist looking to redesign business card

I'm a makeup artist relocating from Sydney to the Tweed Heads Area. I will be providing makeup services (primarily in bridal/wedding, events) in the Tweed Heads, Gold Coast and Byron Bay areas. I have attached 2 photos to use on the front OR back of the card. I can't decide which photo will work best, so I have provided both for you to decide. I'm open to the idea of a logo creation, or just the business name. Business name is;
Marlena Ruth Copley Makeup Artist
or
Marlena Copley Makeup Artist
I will need a space for ABN, mobile number, email address and website address.
I'm open to the photo being either colour or B&W.
Font and background colour could be B&W or another colour, again I'm looking for something different and creative, which is why I'm posting this ad.
I do like the idea of the photo being panoramic, so the veil material continues off to the side.
I'm excited to see what people come up with!!!
Target Market(s)
ladies
Industry/Entity Type
Business
Contact Information for Business Card
or

```html
<!DOCTYPE html>
<html lang="en">
<head>
<meta charset="utf-8">
<title>Marlena Copley Makeup Artist – Business Card</title>
<link rel="stylesheet" href="https://fonts.googleapis.com/css2?family=Great+Vibes&family=Cinzel:wght@400&family=Open+Sans:wght@400&display=swap">
<style>
  :root {
    --page: #ffffff;
    --card: #000000;
    --accent: #e0252c;
    --ink-light: #ffffff;
    --photo-light: #f4ecec;
    --photo-mid: #e9d2cc;
    --photo-warm: #c9977c;
  }
  * { box-sizing: border-box; margin: 0; padding: 0; }
  html, body {
    width: 999px; height: 1200px; overflow: hidden;
    background: var(--page);
  }
  .canvas { position: relative; width: 999px; height: 1200px; }

  .card {
    position: absolute; left: 58px; width: 908px; height: 518px;
    background: var(--card); overflow: hidden;
  }
  .card--front { top: 78px; }
  .card--back { top: 622px; }

  .brand-name {
    position: absolute;
    font-family: "Great Vibes", cursive;
    color: var(--accent);
    white-space: nowrap;
    line-height: 1;
  }
  .brand-role {
    position: absolute;
    font-family: "Cinzel", serif;
    color: var(--ink-light);
    white-space: nowrap;
    line-height: 1;
    letter-spacing: 1px;
  }

  .card--front .brand-name { left: 52px; top: 34px; font-size: 76px; }
  .card--front .brand-role { right: 441px; top: 112px; font-size: 29px; }

  .address {
    position: absolute; left: 58px; top: 296px;
    font-family: "Open Sans", sans-serif; font-size: 23px;
    line-height: 33px; color: var(--ink-light);
  }
  .contact-list {
    position: absolute; left: 58px; top: 383px; list-style: none;
    font-family: "Open Sans", sans-serif; font-size: 23px; color: var(--ink-light);
  }
  .contact-list li { display: flex; align-items: center; height: 34.5px; }
  .contact-list svg { width: 24px; height: 24px; margin-right: 25px; flex: none; }

  .accent-bar {
    position: absolute; left: 523px; top: 0; width: 10px; height: 518px;
    background: var(--accent);
  }
  .portrait {
    position: absolute; left: 533px; top: 0; width: 375px; height: 518px;
    background:
      radial-gradient(ellipse 30% 30% at 50% 38%, var(--photo-warm), transparent 70%),
      linear-gradient(180deg, var(--photo-light) 0%, var(--photo-mid) 55%, #fbf8f8 100%);
  }

  .card--back .brand-name { left: 170px; top: 198px; font-size: 96px; }
  .card--back .brand-role { right: 174px; top: 296px; font-size: 40px; }
</style>
</head>
<body>
<main class="canvas">
  <section class="card card--front">
    <h1 class="brand-name">Marlena Copley</h1>
    <p class="brand-role">Makeup Artist</p>

    <p class="address">suit # 00, Lorem ipsum<br>Lorem Lorem ipsum</p>

    <ul class="contact-list">
      <li>
        <svg viewBox="0 0 24 24" aria-hidden="true"><path fill="#fff" d="M6.6 2.5l3 3.4-1.8 2.4c1.2 2.6 3.3 4.7 5.9 5.9l2.4-1.8 3.4 3-2 3.6C10.3 19.5 4.5 13.7 3 6.5z"/><path fill="none" stroke="#fff" stroke-width="1.6" stroke-linecap="round" d="M14 3.5a7 7 0 0 1 6.5 6.5M14 7a3.5 3.5 0 0 1 3 3"/></svg>
        000-000-0000
      </li>
      <li>
        <svg viewBox="0 0 24 24" aria-hidden="true"><path fill="#fff" d="M2 10l10-7 10 7v11H2z"/><path fill="#000" d="M4.5 11L12 16l7.5-5v1.5L12 17.5 4.5 12.5z"/></svg>
        abcde@marlenacopley.com
      </li>
      <li>
        <svg viewBox="0 0 24 24" aria-hidden="true"><g fill="none" stroke="#fff" stroke-width="1.6"><circle cx="12" cy="12" r="9.5"/><ellipse cx="12" cy="12" rx="4.2" ry="9.5"/><path d="M2.5 12h19M4 7h16M4 17h16"/></g></svg>
        www.marlenacopley.com
      </li>
    </ul>

    <div class="accent-bar"></div>
    <div class="portrait" role="img" aria-label="Portrait photo of the makeup artist in a white veil wrap against a light backdrop"></div>
  </section>

  <section class="card card--back">
    <h2 class="brand-name">Marlena Copley</h2>
    <p class="brand-role">Makeup Artist</p>
  </section>
</main>
</body>
</html>
```